brochure with prices and map

I need a hairdressing brochure designed to hand out to customers to advise of costs and where we are situated.

Website also needs to be included: www.bluequarryhairdesign.com
Please see website for prices and services

The final design should express that we have perth prices right here in Karratha and our address and walk in services

```html
<!DOCTYPE html>
<html lang="en">
<head>
<meta charset="utf-8">
<title>Blue Quarry Hair Design – Brochure</title>
<link rel="stylesheet" href="https://fonts.googleapis.com/css2?family=Josefin+Sans:wght@300;400;600&family=Pinyon+Script&family=Arimo:wght@400;700&family=Cinzel:wght@400&family=Cormorant+Garamond:wght@500&display=swap">
<style>
:root{
  --page:#ffffff;
  --slate:#2d3647;
  --slate-light:#4f5b70;
  --teal:#4ff0d2;
  --pink:#ec1660;
  --white:#ffffff;
  --muted:#d9dde4;
  --photo-dark:#1b2230;
  --photo-mid:#8d97ab;
  --map-base:#ece7dc;
  --map-road:#f7f4ee;
}
*{margin:0;padding:0;box-sizing:border-box}
html,body{width:1200px;height:932px;overflow:hidden;background:var(--page)}
.canvas{position:relative;width:1200px;height:932px}
.panel{position:absolute;left:63px;width:1060px;background:var(--slate);overflow:hidden}
.panel--hero{top:20px;height:435px;background:radial-gradient(ellipse 420px 380px at 300px 150px,var(--slate-light),var(--slate) 80%)}
.panel--prices{top:473px;height:437px}
.hero-photo{position:absolute;left:0;top:0;width:400px;height:435px;
  background:radial-gradient(ellipse 200px 260px at 200px 180px,var(--photo-mid),transparent 75%),linear-gradient(180deg,var(--slate-light),var(--photo-dark))}
.hero-brand{position:absolute;left:32px;top:355px;font-family:"Josefin Sans",sans-serif;font-weight:300;font-size:44px;color:var(--white)}
.contact-web{position:absolute;right:46px;top:27px;font-family:"Arimo",sans-serif;font-size:18px;letter-spacing:.6px;color:var(--white)}
.contact-phone{position:absolute;right:46px;top:50px;font-family:"Arimo",sans-serif;font-size:24px;letter-spacing:1.5px;color:var(--white)}
.headline{font-family:"Josefin Sans",sans-serif;font-weight:300;color:var(--white);position:absolute}
.headline--intro{left:399px;top:78px;font-size:33px;letter-spacing:2px}
.headline--new{left:540px;top:118px;font-size:48px;font-weight:400;letter-spacing:2px}
.headline--new .accent{color:var(--teal)}
.headline--amp{left:728px;top:66px;font-family:"Pinyon Script",cursive;font-size:96px;color:var(--white)}
.headline--better{left:545px;top:172px;font-size:62px;letter-spacing:4px;color:var(--teal)}
.intro{position:absolute;left:412px;top:267px;width:600px;font-family:"Arimo",sans-serif;font-size:14.6px;line-height:19.2px;letter-spacing:.7px;color:var(--white);text-align:justify}
.intro .name{color:var(--teal)}
.price-list{position:absolute;left:60px;top:0;font-family:"Arimo",sans-serif;font-weight:700;font-size:11px;line-height:12px;color:var(--white)}
.price-list p{position:absolute;white-space:nowrap}
.price-list .section{color:var(--pink);letter-spacing:.6px}
.price-list .item{color:var(--teal)}
.price-list .note{font-weight:400;color:var(--white)}
.slogan{position:absolute;left:520px;top:55px;width:476px;text-align:center;font-family:"Arimo",sans-serif;font-weight:700;font-size:26px;line-height:38px;letter-spacing:1.6px;color:var(--white)}
.brand-block{position:absolute;left:420px;top:180px;width:300px;text-align:center;color:var(--white)}
.brand-name{font-family:"Josefin Sans",sans-serif;font-weight:300;font-size:40px;line-height:46px}
.brand-sub{font-family:"Cormorant Garamond",serif;font-weight:500;font-size:19px;letter-spacing:8px;margin-top:2px}
.brand-rule{width:240px;height:1px;margin:6px auto 6px;background:linear-gradient(90deg,transparent,var(--muted),transparent)}
.brand-phone{font-family:"Cormorant Garamond",serif;font-weight:500;font-size:21px;letter-spacing:1px}
.brand-address{font-family:"Cinzel",serif;font-size:13px;line-height:16px;margin-top:4px}
.landmark{position:absolute;left:420px;top:356px;width:300px;text-align:center;font-family:"Arimo",sans-serif;font-size:16px;letter-spacing:1.4px;color:var(--white)}
.map{position:absolute;left:748px;top:207px;width:257px;height:186px;
  background:linear-gradient(125deg,var(--map-base) 0 55%,var(--map-road) 55% 60%,var(--map-base) 60%)}
</style>
</head>
<body>
<div class="canvas">
  <section class="panel panel--hero">
    <div class="hero-photo" role="img" aria-label="Portrait of a woman with long glossy dark hair and a straight fringe"></div>
    <div class="hero-brand">Blue Quarry</div>
    <div class="contact-web">www.bluequarryhairdesign.com</div>
    <div class="contact-phone">08 9140 2765</div>
    <div class="headline headline--intro">Are You Ready for</div>
    <div class="headline headline--new">A <span class="accent">NEW</span></div>
    <div class="headline headline--amp">&amp;</div>
    <div class="headline headline--better">BETTER YOU?</div>
    <p class="intro"><span class="name">Blue Quarry Hair Design</span> one of the ‘oldest’ salons in Karratha offering exceptional service and quality. Come in and be pampered by our highly trained staff. Our salon is under going a renovation and we are adding a Mens Barber section specifically designed for walk in appointments. For the Ladies we have created a beautiful environment where you can relax and forget about all your worries while our friendly staff will cater to all your hair and beauty needs while you are transported to a world of relaxation and tranquility.</p>
  </section>

  <section class="panel panel--prices">
    <div class="price-list">
      <p class="section" style="top:31px">CUT &amp; STYLING</p>
      <p class="item" style="top:63px">HAIRCUT</p>
      <p class="item" style="top:73px">HAIRCUTS INCLUDE SHAMPOO, BLOWDRY &amp; STYLE <span class="note">- from</span> <b style="color:var(--white)">$65.00</b></p>
      <p class="item" style="top:95px">Wash &amp; Blow Dry <span class="note">- from</span> <b style="color:var(--white)">$40.00</b></p>
      <p class="item" style="top:107px">Mens Cuts <span class="note">- from</span> <b style="color:var(--white)">$27.00</b></p>
      <p class="item" style="top:119px">Clipper Cut <span class="note">- from</span> <b style="color:var(--white)">$17.00</b></p>
      <p class="item" style="top:131px">Colours starting at <span class="note">- from</span> <b style="color:var(--white)">$55.00</b></p>
      <p class="item" style="top:143px">Foils starting at <span class="note">- from</span> <b style="color:var(--white)">$70.00</b></p>
      <p class="section" style="top:175px">HAIR &amp; SCALP TREATMENT</p>
      <p class="item" style="top:201px">Straightening permanent <span class="note">-</span> <b style="color:var(--white)">$300</b> <span class="note">and up</span></p>
      <p class="item" style="top:213px">Deep Treatment Mask <span class="note">- from</span> <b style="color:var(--white)">$15</b></p>
      <p class="item" style="top:225px">Perm <span class="note">- from</span> <b style="color:var(--white)">$50</b> <span class="note">(fringe)</span></p>
      <p class="item" style="top:237px">Treatments for maintaining hair <span class="note">- from</span> <b style="color:var(--white)">$15</b></p>
      <p class="section" style="top:269px">SPECIAL SERVICES</p>
      <p class="item" style="top:300px">Up Do <span class="note">- from</span> <b style="color:var(--white)">$85</b> <span class="note">and up</span></p>
      <p class="item" style="top:321px">Hair Extensions <span class="note">- from</span> <b style="color:var(--white)">$300</b> <span class="note">(deposit required)</span></p>
      <p class="item" style="top:332px">Weekly specials <span class="note">-</span> <b style="color:var(--white)">$POA</b></p>
      <p class="item" style="top:342px">Bridal and Formal Occasions <span class="note">- Affordable price to be discussed</span></p>
      <p class="note" style="top:352px;left:166px">with expert consultant</p>
      <p class="item" style="top:384px">Ear piercing starts <span class="note">from</span> <b style="color:var(--white)">$30</b> <span class="note">- service price includes earrings.</span></p>
      <p class="item" style="top:395px">Nose piercing starts <span class="note">from</span> <b style="color:var(--white)">$50</b> <span class="note">- service price includes earring</span></p>
    </div>

    <h2 class="slogan">PERTH PRICES<br>RIGHT HERE IN KARRATHA</h2>

    <div class="brand-block">
      <div class="brand-name">Blue Quarry</div>
      <div class="brand-sub">Hair Design</div>
      <div class="brand-rule"></div>
      <div class="brand-phone">PH (08) 9140 2765</div>
      <div class="brand-address">3/22 Ridgeway Place<br>Karratha WA 6714</div>
    </div>
    <div class="landmark">LandMark – Town Square</div>

    <div class="map" role="img" aria-label="Street map of central Karratha showing the salon location"></div>
  </section>
</div>
</body>
</html>
```